Two documents one design language.

We are a small insurance broker who is committed to being open and transparent as possible with our customers.

For years, we have used plain word documents (see attachments) for our Policy Wording and our Terms of Business.

But now think we can do better and these plain documents are falling behind what our competitors are offering.

So we are now looking for both these documents to be professionally designed using the same design language for both.

We are putting few constraints on the design, but we do have some:
- It must be done in word as the wording can be changed at any time, so we must be able to maintain the documents ourselves.
- Any pictures or graphics you use must be royalty free so we can re-produce with any complications.
- Any pictures or graphics you use must been supplied as part of the package.
- You MUST NOT change any wording or grammar, it's not ours to change, its the insurers wording and HAS to be agreed with them.
- You must not split any any paragraph or bullet point over two pages.
- We are an insurance broker so what ever design you use, must look professional and inspire confidence... I.e. if you read it your thoughts turn to, these people are approachable, know what they are doing and will look after me.
- We specialise in musical instrument insurance, so we are looking for musical theming.

```html
<!DOCTYPE html>
<html lang="en">
<head>
<meta charset="utf-8">
<title>Miles Carver Insurance – Policy Wording spreads</title>
<link rel="stylesheet" href="https://fonts.googleapis.com/css2?family=Poppins:wght@400;500;600;700&display=swap">
<style>
  :root{
    --pink:#e8849e;
    --pink-soft:#f6d3dd;
    --charcoal:#4a4748;
    --ink:#3b3a3b;
    --paper:#ffffff;
    --backdrop:#e4e4e4;
  }
  *{box-sizing:border-box;margin:0;padding:0}
  html,body{width:1200px;height:1200px;overflow:hidden}
  body{background:var(--backdrop);font-family:"Poppins",sans-serif;color:var(--ink);position:relative}
  .page{position:absolute;width:338px;height:481px;background:var(--paper);overflow:hidden}
  .page--cover{left:62px;top:69px}
  .page--contents{left:431px;top:69px}
  .page--definitions{left:800px;top:69px}
  .page--information{left:62px;top:650px}
  .page--duties{left:431px;top:650px}

  .side-bar{position:absolute;left:0;top:0;width:16px;background:var(--charcoal)}
  .top-band{position:absolute;top:21px;height:14px;background:var(--pink)}

  /* cover */
  .brand{position:absolute;left:35px;top:58px;display:flex;align-items:center;gap:6px}
  .brand__dot{width:10px;height:10px;border-radius:50%;background:var(--pink)}
  .brand__name{font-weight:700;font-size:17px;line-height:1.05;color:var(--charcoal);letter-spacing:.5px;width:140px}
  .cover-wave{position:absolute;left:0;top:0}
  .cover-art{position:absolute;left:82px;top:104px;width:200px;height:310px;border-radius:40% 40% 30% 30%;
    background:radial-gradient(ellipse at 50% 45%,var(--pink-soft),rgba(246,211,221,.15) 70%,transparent 72%)}
  .cover-title{position:absolute;left:35px;top:306px;font-weight:700;font-size:21px;line-height:1.1;color:var(--charcoal)}

  /* contents */
  .contents-title{position:absolute;left:41px;top:48px;font-weight:600;font-size:17px;color:var(--charcoal)}
  .toc{position:absolute;left:41px;top:94px;width:254px;list-style:none}
  .toc li{display:flex;align-items:baseline;font-size:6.4px;height:15.3px;color:var(--ink);text-transform:uppercase}
  .toc .leader{flex:1;border-bottom:1px dotted #999;margin:0 3px}
  .contents-wave{position:absolute;left:0;bottom:0}

  /* text pages */
  .page-heading{position:absolute;left:35px;font-weight:700;color:#1f1e1f;text-transform:uppercase}
  .body{position:absolute;font-size:5.6px;line-height:1.4;color:var(--ink)}
  .body p{margin-bottom:5px}
  .body dt{font-weight:700;font-size:6px;text-transform:uppercase;color:#1f1e1f}
  .body dd{margin-bottom:6px}
  .body ul{margin:0 0 5px 10px}
  .body ol{margin-left:0;list-style:none}
  .body ol li{margin-bottom:5px}

  .photo{position:absolute}
  .photo--harpist{left:194px;top:225px;width:144px;height:256px;background:linear-gradient(160deg,#d9d9d9,#6d6d6d 60%,#2d2d2d)}
  .accent-block{position:absolute;left:116px;top:425px;width:96px;height:27px;background:var(--pink)}
  .photo--duo{left:16px;top:19px;width:322px;height:200px;background:linear-gradient(180deg,#e9b7bf,#c99a7e 45%,#8a6a55)}
  .label{position:absolute;left:34px;top:194px;width:141px;height:27px;background:var(--pink);color:#fff;
    font-weight:700;font-size:14px;display:flex;align-items:center;padding-left:10px;text-transform:uppercase}
</style>
</head>
<body>

<!-- Cover -->
<section class="page page--cover">
  <svg class="cover-wave" width="338" height="481" viewBox="0 0 338 481" aria-hidden="true">
    <path d="M0,150 C40,190 130,260 170,350 C195,410 215,450 232,481 L0,481 Z" fill="var(--pink)"/>
  </svg>
  <div class="brand"><span class="brand__name">MILES CARVER INSURANCE</span><span class="brand__dot"></span></div>
  <div class="cover-art" role="img" aria-label="Line illustration of a cherub playing a harp"></div>
  <h1 class="cover-title">POLICY<br>WORDING</h1>
</section>

<!-- Contents -->
<section class="page page--contents">
  <h2 class="contents-title">Contents</h2>
  <ol class="toc">
    <li>Definitions<span class="leader"></span>02</li>
    <li>Policy Overview<span class="leader"></span>03</li>
    <li>Certificate of Insurance (Public Liability)<span class="leader"></span>04</li>
    <li>Certificate of Insurance (Musical Instruments and accessories)<span class="leader"></span>06</li>
    <li>Schedule<span class="leader"></span>08</li>
    <li>Information you have given us<span class="leader"></span>09</li>
    <li>Your duties<span class="leader"></span>10</li>
    <li>The cover provided<span class="leader"></span>11</li>
    <li>Public liability cover<span class="leader"></span>13</li>
    <li>Exclusions<span class="leader"></span>15</li>
    <li>How to amend your policy<span class="leader"></span>23</li>
    <li>Renewing your policy<span class="leader"></span>23</li>
    <li>How to cancel your policy<span class="leader"></span>24</li>
    <li>Claims conditions<span class="leader"></span>26</li>
    <li>How to make a complaint<span class="leader"></span>29</li>
    <li>Authorisation &amp; regulation<span class="leader"></span>32</li>
    <li>Privacy notices<span class="leader"></span>33</li>
  </ol>
  <svg class="contents-wave" width="338" height="140" viewBox="0 0 338 140" aria-hidden="true">
    <path d="M18,140 C30,80 70,40 130,40 C180,40 170,10 230,8 L338,6 L338,140 Z" fill="var(--pink)"/>
    <path d="M18,140 C26,95 55,60 100,50 C70,70 48,100 40,140 Z" fill="var(--charcoal)"/>
  </svg>
</section>

<!-- Definitions -->
<section class="page page--definitions">
  <div class="side-bar" style="height:415px"></div>
  <div class="top-band" style="left:19px;width:256px"></div>
  <h2 class="page-heading" style="top:54px;font-size:17px">Definitions</h2>
  <dl class="body" style="left:35px;top:84px;width:270px">
    <p>Wherever the following words appear in CAPITALS in this policy document they will have the meanings shown below.</p>
    <dt>Endorsement(s)</dt><dd>Any variations or additions to the terms of this insurance.</dd>
    <dt>Period of Insurance</dt><dd>The length of time for which this insurance is in force as shown in the SCHEDULE, or until cancelled.</dd>
    <dt>Premises</dt><dd>The location stated in the SCHEDULE where the INSURED PROPERTY is usually kept.</dd>
    <dt>Property Insured</dt><dd>The musical instrument(s), equipment and accessories as detailed in the SCHEDULE.</dd>
    <dt>Schedule</dt><dd>The SCHEDULE is part of the policy. It shows details of YOU, the PROPERTY INSURED, the sums insured, the level of cover, the PERIOD OF INSURANCE and the sections of this insurance which apply.</dd>
    <dt>We/Our/Us</dt><dd>a) Northshore Insurance UK Ltd<br>b) TRV Management Limited at all times as authorised underwriting agents and administrators (and for no other purpose) for Harbour UK Speciality on behalf of Northshore Insurance UK Ltd with no liability under this Policy<br>c) Miles Carver Insurance Services as administrators under this policy.</dd>
    <dt>You/Your</dt><dd>The person(s) named as the Insured in the SCHEDULE and members of YOUR immediate family.</dd>
    <dt>Friend</dt><dd>A third party whom YOU entrust the PROPERTY INSURED who may transport/use/store in YOUR absence and for which YOU do not receive any commercial reward.</dd>
    <dt>Teacher</dt><dd>The person who YOU regularly receive instruction on the use of the PROPERTY INSURED and is suitably qualified.</dd>
  </dl>
</section>

<!-- Information you have given us -->
<section class="page page--information">
  <div class="side-bar" style="height:481px;width:19px"></div>
  <div class="top-band" style="left:19px;width:319px"></div>
  <h2 class="page-heading" style="top:55px;font-size:14.5px">Information you have given us</h2>
  <div class="body" style="left:35px;top:82px;width:280px">
    <p>In deciding to accept this insurance and in setting the terms and premium, WE have relied on the information YOU have given US. YOU must take care when answering any questions WE ask by ensuring that all information provided is accurate and complete.</p>
    <p>If WE establish that YOU deliberately or recklessly provided US with false or misleading information WE will treat this insurance as if it never existed and decline all claims.</p>
    <p>If WE establish that YOU carelessly provided US with false or misleading information it could adversely affect YOUR insurance and any claim. For example WE may:</p>
    <ul>
      <li>treat this insurance as if it had never existed and refuse to pay all claims and return the premium paid. WE will only do this if WE provided YOU with insurance cover which WE would not otherwise have offered; or</li>
      <li>amend the terms of YOUR insurance. WE may apply these amended terms as if they were already in place if a claim has been adversely impacted by YOUR carelessness; or</li>
      <li>charge YOU more for YOUR insurance or reduce the amount WE pay on a claim in the proportion the premium YOU have paid bears to the premium WE would have charged YOU; or</li>
      <li>cancel YOUR insurance in accordance with the HOW TO CANCEL THIS POLICY section within this policy document.</li>
    </ul>
  </div>
  <div class="body" style="left:35px;top:262px;width:140px">
    <p>WE or Miles Carver Insurance Services will write to YOU if WE:</p>
    <ul>
      <li>intend to treat this insurance as if it never existed; or</li>
      <li>need to amend the terms of YOUR insurance; or</li>
      <li>require YOU to pay more for YOUR insurance.</li>
    </ul>
  </div>
  <div class="photo photo--harpist" role="img" aria-label="Black and white photograph of a harpist seated with her harp"></div>
  <div class="accent-block"></div>
</section>

<!-- Your duties -->
<section class="page page--duties">
  <div class="side-bar" style="height:240px"></div>
  <div class="photo photo--duo" role="img" aria-label="Photograph of two harpists among pink flowers, seen from above"></div>
  <div class="label">Your duties</div>
  <div class="body" style="left:34px;top:238px;width:280px">
    <p>These are the conditions of the insurance YOU will need to meet as YOUR part of this insurance contract. If YOU do not comply a claim may be rejected or payment could be reduced. In some instances, YOUR policy might be invalid.</p>
    <ol>
      <li>1.&nbsp;&nbsp;PROTECTION MAINTENANCE CLAUSE<br>YOU must ensure that all protections provided for the security of the items covered under this insurance are maintained in good working order and are in full and effective operation whenever PREMISES are without an authorised occupant.</li>
      <li>2.&nbsp;&nbsp;REASONABLE CARE<br>YOU must take all reasonable steps to prevent accidents, loss, destruction or damage and must maintain the PROPERTY INSURED in a good state of repair and condition.</li>
      <li>3.&nbsp;&nbsp;CHANGES IN YOUR CIRCUMSTANCES<br>YOU must notify Miles Carver Insurance Services as soon as possible about any changes in the information YOU have provided to US which happen before or during any PERIOD OF INSURANCE. Examples of things which WE need to know about include (but are not limited to): any change of address; any changes in YOUR sums insured; if YOU or any person living with YOU are convicted of any offence (other than driving offences) or are declared bankrupt.</li>
      <li>4.&nbsp;&nbsp;YOU must ensure that all PROPERTY INSURED is adequately packed in suitable carrying cases to provide protection when removed from the PREMISES.</li>
      <li>5.&nbsp;&nbsp;If YOU wish to take up 'On Loan/Hire' cover under this policy YOU must take adequate precautions to assess the identity of the person YOU are loaning the instrument to and retain evidence of their identity, including their address.</li>
      <li>6.&nbsp;&nbsp;YOU must be able to prove ownership or legal responsibility for the PROPERTY INSURED in the event of a claim. This may take the form of a valuation from a suitably qualified valuer (preferably dated within the last 5 years) or a purchase receipt.</li>
    </ol>
  </div>
</section>

</body>
</html>
```